Vantorique Business Card and Letter Head

We are a leadership assessment consultancy based in Sydney, Australia. We help executive-level decison-makers select leaders for more senior level roles in corporate and government organisations. Our methodology is based on the latest research from the field of neuroscience.
We need a business card design and matching letter head that presents our company, Vantorique, as a:
1. trusted adviser to senior executive-level decison makers
2. niche consultancy who are experts in the field of assessing leadership talent
3. results-focused solution provider who balance scientific methods with pragmatic solutions
The following company details should be used in all designs:
Company Name: Vantorique
Details (for business card):
Daniel Prewett
Senior Talent Adviser
Level 17, Marrowby Tower
14 Tallowin Square
Sydney, NSW 2000 Australia
Phone: 1300 582 714
Mobile: 0412 637 208
Email: daniel.prewett@vantorique.com.au
Website: vantorique.com.au
I have attached the logo for Vantorique (for both a white and black background) - your business card and letter head designs must incoporate this logo and colour scheme.
Thanks for your interest in this project, I'm looking forward to receiving your ideas.
Regards,
Daniel
Target Market(s)
Executive-level decison-makers in corporate and government organisations (e.g., CEO, VP, Head of Human Resources)
Industry/Entity Type
Leadership
Look and feel
Each slider illustrates characteristics of the customer's brand and the style your logo design should communicate.

```html
<!DOCTYPE html>
<html lang="en">
<head>
<meta charset="utf-8">
<title>Vantorique Business Card</title>
<link rel="stylesheet" href="https://fonts.googleapis.com/css2?family=Arimo:wght@400;700&display=swap">
<style>
  :root {
    --backdrop: #9b9b9b;
    --card-dark: #2b2b2c;
    --card-dark-edge: #232324;
    --card-light: #f1f1f1;
    --card-light-edge: #e2e2e2;
    --accent-red: #b51a14;
    --ink-dark: #2a2a2b;
    --ink-light: #ffffff;
    --rule: #8c8c8c;
  }
  * { box-sizing: border-box; margin: 0; padding: 0; }
  html, body { width: 1200px; height: 720px; overflow: hidden; }
  body {
    background: var(--backdrop);
    font-family: "Arimo", Arial, sans-serif;
    position: relative;
  }
  .card {
    position: absolute;
    top: 206px;
    width: 540px;
    height: 308px;
    overflow: hidden;
    box-shadow: 0 10px 24px rgba(0,0,0,0.28);
  }
  .card-front { left: 45px; background: var(--card-dark); }
  .card-back {
    left: 615px;
    background: linear-gradient(135deg, var(--card-dark) 0%, var(--card-dark-edge) 100%);
  }

  /* front */
  .front-header {
    position: absolute; left: 0; top: 0; width: 100%; height: 138px;
    background: linear-gradient(180deg, #fafafa 0%, var(--card-light) 60%, var(--card-light-edge) 100%);
    border-bottom: 4px solid var(--accent-red);
  }
  .pointer {
    position: absolute; left: 50px; top: 142px;
    width: 0; height: 0;
    border-left: 9px solid transparent;
    border-right: 9px solid transparent;
    border-top: 9px solid var(--accent-red);
  }
  .brand {
    position: absolute; display: flex; align-items: center; gap: 14px;
  }
  .brand-mark { width: 22px; height: 22px; background: var(--accent-red); }
  .brand-name { font-weight: 700; letter-spacing: -0.5px; line-height: 1; }
  .front-header .brand { left: 150px; top: 46px; }
  .front-header .brand-name { font-size: 46px; color: var(--ink-dark); }

  .person {
    position: absolute; left: 36px; top: 176px;
  }
  .person-name { color: var(--accent-red); font-weight: 700; font-size: 19px; }
  .person-role { color: var(--ink-light); font-size: 16px; margin-top: 5px; }
  .divider {
    position: absolute; left: 238px; top: 166px; width: 1px; height: 112px;
    background: var(--rule);
  }
  .contact {
    position: absolute; left: 260px; top: 166px;
    color: var(--ink-light); font-size: 13.5px; line-height: 18px;
  }
  .contact-address { margin-bottom: 4px; }
  .contact-line { display: flex; align-items: center; gap: 8px; }
  .contact-line svg { width: 11px; height: 11px; flex: none; }

  /* back */
  .card-back .brand { left: 50%; top: 112px; transform: translateX(-50%); }
  .card-back .brand-name { font-size: 50px; color: var(--ink-light); }
  .website {
    position: absolute; right: 30px; bottom: 26px;
    color: var(--ink-light); font-size: 17px; font-weight: 700;
  }
</style>
</head>
<body>
  <section class="card card-front" aria-label="Business card front">
    <header class="front-header">
      <div class="brand">
        <span class="brand-mark" aria-hidden="true"></span>
        <span class="brand-name">Vantorique</span>
      </div>
    </header>
    <span class="pointer" aria-hidden="true"></span>

    <div class="person">
      <p class="person-name">Daniel Prewett</p>
      <p class="person-role">Senior Talent Adviser</p>
    </div>

    <span class="divider" aria-hidden="true"></span>

    <div class="contact">
      <p class="contact-address">Level 17, Marrowby Tower<br>14 Tallowin Square, Sydney,<br>NSW 2000 Australia</p>
      <p class="contact-line">
        <svg viewBox="0 0 12 12" aria-hidden="true"><rect width="12" height="12" rx="2" fill="var(--accent-red)"/><path d="M3.5 2.8c.4-.3.9-.2 1.1.2l.6 1.2c.2.4 0 .7-.3.9l-.3.2c.4.9 1 1.5 1.9 1.9l.2-.3c.2-.3.6-.4.9-.3l1.2.6c.4.2.5.7.2 1.1l-.5.6c-.4.4-1 .5-1.5.3C5.2 8.3 3.7 6.8 2.9 5c-.2-.5-.1-1.1.3-1.5z" fill="#fff"/></svg>
        1300 582 714
      </p>
      <p class="contact-line">
        <svg viewBox="0 0 12 12" aria-hidden="true"><rect width="12" height="12" rx="2" fill="var(--accent-red)"/><rect x="4" y="2" width="4" height="8" rx="0.8" fill="#fff"/><rect x="4.7" y="3" width="2.6" height="4.8" fill="var(--accent-red)"/></svg>
        0412 637 208
      </p>
      <p class="contact-line">
        <svg viewBox="0 0 12 12" aria-hidden="true"><rect width="12" height="12" rx="2" fill="var(--accent-red)"/><rect x="2.2" y="3.5" width="7.6" height="5" fill="#fff"/><path d="M2.2 3.5 6 6.4l3.8-2.9" fill="none" stroke="var(--accent-red)" stroke-width="0.9"/></svg>
        daniel.prewett@vantorique.com.au
      </p>
    </div>
  </section>

  <section class="card card-back" aria-label="Business card back">
    <div class="brand">
      <span class="brand-mark" aria-hidden="true"></span>
      <span class="brand-name">Vantorique</span>
    </div>
    <p class="website">vantorique.com.au</p>
  </section>
</body>
</html>
```